Coastal waterside shopping complex needs a billboard sign

"Harbour Verge" is the name of a building which comprises 4 shops in a coastal waterside location. We need a 2440mm (Wide) x 1100mm (High) "Harbour Verge" billboard design that will fit with the coastal theme but is modern and contemporary, positioning the building as a high class mini shopping complex.

The photo below is for reference only. We only need a design for the "Harbour Verge" sign.

The end product will need to be an EPS scalable vector file.

```html
<!DOCTYPE html>
<html lang="en">
<head>
<meta charset="UTF-8">
<title>Harbour Verge Billboard</title>
<link rel="stylesheet" href="https://fonts.googleapis.com/css2?family=Bebas+Neue&display=swap">
<style>
  :root {
    --backdrop: #8c8c8c;
    --sign-blue: #0a0091;
    --sign-text: #ffffff;
  }
  html, body {
    margin: 0;
    padding: 0;
    width: 1200px;
    height: 1200px;
    overflow: hidden;
    background: var(--backdrop);
  }
  .billboard {
    position: absolute;
    left: 80px;
    top: 366px;
    width: 1040px;
    height: 468px;
    background: var(--sign-blue);
    box-shadow: 3px 4px 8px rgba(0, 0, 0, 0.35);
    text-align: center;
  }
  .billboard-name {
    position: absolute;
    left: 0;
    right: 0;
    top: 135px;
    margin: 0;
    font-weight: 400;
  }
  .billboard-name span {
    display: inline-block;
    font-family: "Bebas Neue", "Arial Narrow", sans-serif;
    font-size: 208px;
    line-height: 0.88;
    letter-spacing: 1px;
    color: var(--sign-text);
    border-bottom: 6px solid var(--sign-text);
  }
</style>
</head>
<body>
  <div class="billboard">
    <h1 class="billboard-name"><span>Harbour Verge</span></h1>
  </div>
</body>
</html>
```